Business Card for a finance professional

I need a business card design to introduce myself to a professional networking (mainly banks) and potential companies to hire and remember me. I would like to use black, grey, white and maybe gold/silver colors and maybe something with my initials(L R B F T). The final design should communicate seriousness, profissionalism and something innovative.

The basic informations in the card are: Name, e-mail, phone number and linkedin. (I'm thinking to put some directly short link to my linkedin account or maybe some app - non QR Code - to add my contacts to a phone directly.)

My name is Mariana Lopes Barbosa Ferraz da Trindade (I prefer to use only 'Mariana Lopes' or 'Mariana Trindade' but i'm open to other suggestions) and I have 26 years old (just if it helps to build based in my age).
Updates

Dear designers, I wish to thank your participation in this project! It was very difficult to choose one! Thank your for your work! Best regards and success. Mariana

Target Market(s)

Potential hires and big companies.

Industry/Entity Type

Finance

Requirements
Must have
• The informations required at the business card are:
Name: Mariana Lopes B. F. da Trindade
Email: mariana.lbf.trindade@caixapostal.example
Phone: +55 61 9043 5718
LinkedIn: http://br.redeprofissa.example/in/marianalt/
Nice to have
• Modern and innovative look.
I suggest to use the colors black, grey, white, gold and/or silver, but I'm open to other colors.
Should not have
• A message showing that I need to be hired. It's more to "know me and remember me" than "hire me please".

```html
<!DOCTYPE html>
<html lang="en">
<head>
<meta charset="utf-8">
<title>Business Card – Mariana Lopes B. F. da Trindade</title>
<link href="https://fonts.googleapis.com/css2?family=Didact+Gothic&display=swap" rel="stylesheet">
<style>
  :root {
    --page: #ffffff;
    --paper: #f5f0eb;
    --forest: #25332b;
    --ink-light: #f5f0eb;
    --edge: #8a8a8a;
  }
  html, body {
    margin: 0;
    padding: 0;
    width: 1200px;
    height: 1000px;
    overflow: hidden;
    background: var(--page);
  }
  .canvas {
    position: relative;
    width: 1200px;
    height: 1000px;
    font-family: "Didact Gothic", sans-serif;
  }
  .card {
    position: absolute;
    left: 335px;
    top: 85px;
    width: 531px;
    height: 821px;
    background: var(--paper);
    outline: 1px solid var(--edge);
    overflow: hidden;
  }
  .card__band {
    position: absolute;
    inset: 0;
    width: 531px;
    height: 821px;
  }
  .card__band polygon { fill: var(--forest); }
  .monogram {
    position: absolute;
    left: 38px;
    top: 22px;
    margin: 0;
    font-size: 104px;
    line-height: 1;
    font-weight: 400;
    letter-spacing: 2px;
    color: var(--forest);
  }
  .full-name {
    position: absolute;
    left: 40px;
    top: 146px;
    margin: 0;
    font-size: 22px;
    font-weight: 400;
    color: var(--forest);
    white-space: nowrap;
  }
  .contact {
    position: absolute;
    left: 46px;
    top: 424px;
    margin: 0;
    color: var(--ink-light);
    white-space: nowrap;
  }
  .contact__email { font-size: 21px; line-height: 36px; display: block; }
  .contact__phone { font-size: 26px; line-height: 38px; display: block; }
  .contact__profile { font-size: 19px; display: block; margin-top: 30px; }
</style>
</head>
<body>
  <div class="canvas">
    <section class="card" aria-label="Business card">
      <svg class="card__band" viewBox="0 0 531 821" aria-hidden="true">
        <polygon points="531,130 531,719 293,821 0,821 0,353"/>
      </svg>
      <p class="monogram">LRBFT</p>
      <h1 class="full-name">Mariana Lopes B. F. da Trindade</h1>
      <address class="contact">
        <span class="contact__email">mariana.lbf.trindade@caixapostal.example</span>
        <span class="contact__phone">+55 61 9043 5718</span>
        <span class="contact__profile">http://br.redeprofissa.example/in/marianalt</span>
      </address>
    </section>
  </div>
</body>
</html>
```